I need 2- Sided Tri-Fold Brochure Design for Social Media Marketing Sevices.

Here's the Website URL link: http://www.harborlane4.example/social-media-1/
The brochure should be similar to the site, but it also needs to be very eye-catching as well as professional

I'm looking a very Creative Designer to provide a very unique brochure that will equal sales..

File Type: PSD

Contact me if you have questions

```html
<!DOCTYPE html>
<html lang="en">
<head>
<meta charset="utf-8">
<title>Harbor Lane 4 – Social Media Services Tri-Fold Brochure</title>
<link rel="stylesheet" href="https://fonts.googleapis.com/css2?family=Oswald:wght@500;600;700&family=Tinos:ital,wght@0,400;0,700;1,400;1,700&display=swap">
<style>
  :root {
    --sky-top: #1f7fd4;
    --sky-mid: #4ea6ea;
    --sky-pale: #cfe7fa;
    --paper: #ffffff;
    --paper-shade: #eef3f8;
    --navy: #123b8f;
    --ribbon: #2a67c4;
    --ribbon-light: #3f86dc;
    --ink: #1d2a4a;
    --text-blue: #2460c9;
    --canvas-bg: #e9edf2;
  }
  * { box-sizing: border-box; margin: 0; padding: 0; }
  html, body { width: 1200px; height: 900px; overflow: hidden; background: var(--canvas-bg); }
  body { font-family: "Tinos", Georgia, serif; color: var(--ink); }

  .brochure {
    position: absolute; left: 50px; top: 25px;
    width: 1100px; height: 850px;
    display: grid; grid-template-columns: repeat(3, 1fr);
    box-shadow: 0 10px 30px rgba(20,40,80,.18);
  }
  .panel { position: relative; overflow: hidden; background: var(--paper); }
  .panel + .panel { border-left: 1px solid #d7dfe8; }

  /* Left panel */
  .panel--reasons { background: linear-gradient(180deg, var(--sky-top) 0%, var(--sky-mid) 45%, var(--sky-pale) 72%, var(--paper) 82%); }
  .reasons-banner {
    position: absolute; left: 0; top: 34px; width: 300px; height: 74px;
    background: var(--navy);
    clip-path: polygon(0 0, 88% 0, 100% 50%, 88% 100%, 0 100%);
    display: flex; align-items: center; padding-left: 26px; gap: 10px;
    color: var(--paper); font-family: "Oswald", Arial, sans-serif;
  }
  .reasons-banner__num { font-size: 62px; font-weight: 700; line-height: 1; }
  .reasons-banner__title { font-size: 34px; font-weight: 600; letter-spacing: 1px; }
  .reasons-sub {
    position: absolute; left: 110px; top: 114px; width: 230px;
    font-family: "Oswald", Arial, sans-serif; font-size: 12px; font-weight: 500;
    color: var(--paper); text-transform: uppercase; line-height: 1.3; text-align: right;
  }
  .reasons-intro {
    position: absolute; left: 26px; top: 160px; width: 315px;
    font-size: 15px; line-height: 1.3; color: var(--paper);
  }
  .reasons-list { position: absolute; left: 26px; top: 262px; width: 320px; list-style: none; }
  .reason { display: flex; align-items: center; height: 48px; margin-bottom: 10px; }
  .reason__num {
    width: 40px; height: 40px; background: var(--paper);
    color: var(--ribbon); font-family: "Oswald", Arial, sans-serif;
    font-size: 30px; font-weight: 700; display: flex; align-items: center; justify-content: center;
    border-radius: 4px; flex: none;
  }
  .reason__label {
    flex: 1; height: 40px; margin-left: 6px;
    background: linear-gradient(180deg, var(--ribbon-light), var(--ribbon));
    clip-path: polygon(0 0, 94% 0, 100% 50%, 94% 100%, 0 100%);
    color: var(--paper); font-size: 21px; display: flex; align-items: center; padding-left: 18px;
  }
  .device-art {
    position: absolute; left: 60px; top: 680px; width: 200px; height: 140px;
    border-radius: 12px;
    background: radial-gradient(ellipse at 50% 60%, #1b2a4a 0 28%, #7fb9ea 30%, #e8f1fa 75%);
  }

  /* Middle panel */
  .panel--offer { background: linear-gradient(180deg, var(--sky-pale) 0%, #e6f2fc 52%, var(--paper) 62%); }
  .offer-ribbon {
    position: absolute; left: 60px; top: 40px; width: 280px; padding: 10px 12px;
    text-align: center; color: var(--paper); font-family: "Oswald", Arial, sans-serif;
    background: var(--ribbon); clip-path: polygon(6% 0, 100% 0, 94% 100%, 0 100%);
  }
  .offer-ribbon__small { display: block; font-size: 15px; font-weight: 500; letter-spacing: .5px; }
  .offer-ribbon__big { display: block; font-size: 34px; font-weight: 700; line-height: 1; }
  .offer-copy {
    position: absolute; left: 34px; top: 150px; width: 300px;
    font-size: 16px; line-height: 1.3; text-align: center; color: var(--ink);
  }
  .offer-cloud { position: absolute; left: 50px; top: 262px; width: 270px; height: 170px; }
  .offer-cloud__text {
    position: absolute; inset: 26px 0 0 0; text-align: center;
    font-style: italic; font-size: 21px; line-height: 1.15; color: var(--text-blue);
  }
  .offer-cloud__text b { color: var(--ink); font-weight: 700; }
  .web-bar {
    position: absolute; left: 0; top: 470px; width: 100%; height: 46px;
    background: linear-gradient(180deg, var(--ribbon-light), var(--ribbon));
    color: var(--paper); font-family: "Tinos", Georgia, serif; font-weight: 700; font-size: 21px;
    display: flex; align-items: center; justify-content: center;
  }
  .brand-lockup { display: flex; align-items: center; justify-content: center; gap: 10px; }
  .brand-lockup__name { font-family: "Oswald", Arial, sans-serif; font-weight: 600; color: var(--navy); }
  .brand-lockup__dot { border-radius: 50%; background: var(--ribbon-light); flex: none; }
  .offer-brand { position: absolute; left: 0; top: 545px; width: 100%; }
  .offer-brand .brand-lockup__name { font-size: 30px; }
  .offer-brand .brand-lockup__dot { width: 22px; height: 22px; }
  .offer-address {
    position: absolute; left: 0; top: 600px; width: 100%;
    text-align: center; font-size: 17px; line-height: 1.3; color: var(--ink);
  }

  /* Right panel */
  .panel--cover { background: linear-gradient(180deg, var(--sky-top) 0%, var(--sky-mid) 50%, var(--sky-pale) 64%, var(--paper) 72%); }
  .bubbles-art {
    position: absolute; left: 40px; top: 30px; width: 310px; height: 420px; border-radius: 40px;
    background:
      radial-gradient(circle at 30% 20%, #7fd0ff 0 16%, transparent 17%),
      radial-gradient(circle at 78% 22%, #e0338f 0 13%, transparent 14%),
      radial-gradient(circle at 25% 48%, #8cc63f 0 14%, transparent 15%),
      radial-gradient(circle at 65% 48%, #4b2a8c 0 15%, transparent 16%),
      radial-gradient(circle at 40% 75%, #f07c1e 0 12%, transparent 13%),
      radial-gradient(circle at 80% 76%, #f5c518 0 12%, transparent 13%),
      radial-gradient(circle at 58% 88%, #7b2a8c 0 10%, transparent 11%);
  }
  .cover-banner {
    position: absolute; left: 0; top: 510px; width: 100%; height: 120px;
    background: var(--navy); clip-path: polygon(8% 0, 100% 0, 100% 100%, 0 100%, 0 45%);
    color: var(--paper); font-family: "Oswald", Arial, sans-serif; text-align: right; padding: 12px 24px 0 0;
  }
  .cover-banner__small { display: block; font-size: 32px; font-weight: 600; line-height: 1; }
  .cover-banner__big { display: block; font-size: 60px; font-weight: 700; line-height: 1.05; letter-spacing: 1px; }
  .cover-brand { position: absolute; left: 0; top: 660px; width: 100%; }
  .cover-brand .brand-lockup__name { font-size: 44px; }
  .cover-brand .brand-lockup__dot { width: 30px; height: 30px; }
  .cover-url {
    position: absolute; left: 0; top: 730px; width: 100%;
    text-align: center; font-family: "Oswald", Arial, sans-serif; font-weight: 600; font-size: 26px; color: var(--ink);
  }
</style>
</head>
<body>
<main class="brochure">

  <section class="panel panel--reasons">
    <div class="reasons-banner">
      <span class="reasons-banner__num">7</span>
      <span class="reasons-banner__title">TOP REASONS</span>
    </div>
    <p class="reasons-sub">Why startups should use social media before they launch</p>
    <p class="reasons-intro">Social media is an important part of getting the word out about your startup. Instead of waiting until your product or service is ready consider starting your social media marketing from day one.</p>
    <ol class="reasons-list">
      <li class="reason"><span class="reason__num">1</span><span class="reason__label">Startup Launch Pages</span></li>
      <li class="reason"><span class="reason__num">2</span><span class="reason__label">Engage People</span></li>
      <li class="reason"><span class="reason__num">3</span><span class="reason__label">Bloggers are Important</span></li>
      <li class="reason"><span class="reason__num">4</span><span class="reason__label">Build Your Networking</span></li>
      <li class="reason"><span class="reason__num">5</span><span class="reason__label">Create Great Content</span></li>
      <li class="reason"><span class="reason__num">6</span><span class="reason__label">Build Buzz</span></li>
      <li class="reason"><span class="reason__num">7</span><span class="reason__label">Track Results</span></li>
    </ol>
    <div class="device-art" role="img" aria-label="Illustration of a tablet with colourful social app icons rising from its screen"></div>
  </section>

  <section class="panel panel--offer">
    <div class="offer-ribbon">
      <span class="offer-ribbon__small">WANT TO TAKE YOUR</span>
      <span class="offer-ribbon__big">BUSINESS</span>
      <span class="offer-ribbon__small">TO THE TOP</span>
    </div>
    <p class="offer-copy">The use of social media tools such as Circlebook, WorkNet, ClipCast, Chatterly and Blogs have proven ROI (return on investments) for many businesses and professionals.</p>
    <div class="offer-cloud">
      <svg width="270" height="170" viewBox="0 0 270 170" aria-hidden="true">
        <path d="M50 150 C15 150 10 110 38 100 C20 75 50 45 80 58 C90 25 140 15 160 45 C185 25 230 40 228 75 C262 80 265 130 230 140 C225 160 195 160 180 150 Z"
              fill="#ffffff" stroke="#b9d6f0" stroke-width="2"/>
      </svg>
      <p class="offer-cloud__text"><b>For</b><br>IMMEDIATE<br>DISCOUNTS<br><b>and</b><br>FREE GIFTS</p>
    </div>
    <div class="web-bar">www.harborlane4.example</div>
    <div class="offer-brand brand-lockup">
      <span class="brand-lockup__name">Harbor Lane 4</span>
      <span class="brand-lockup__dot"></span>
    </div>
    <p class="offer-address">Your Address can be written here<br>Didnt find it in your site</p>
  </section>

  <section class="panel panel--cover">
    <div class="bubbles-art" role="img" aria-label="Cluster of colourful speech bubbles carrying social network and communication icons"></div>
    <div class="cover-banner">
      <span class="cover-banner__small">SOCIAL MEDIA</span>
      <span class="cover-banner__big">SERVICES</span>
    </div>
    <div class="cover-brand brand-lockup">
      <span class="brand-lockup__name">Harbor Lane 4</span>
      <span class="brand-lockup__dot"></span>
    </div>
    <p class="cover-url">www.harborlane4.example</p>
  </section>

</main>
</body>
</html>
```